Unternehmen für Ordnung und Sauberkeit am Arbeitsplatz und Produkte zur Produktionsoptimierung benötigt Visitenkarten und Briefpapier
Zielgruppe
Produkte für Ordnung und Sauberkeit am Arbeitsplatz, Organisation von Arbeitsplätzen, Produkte zur Vereinfachung von Arbeitsabläufen, Produkte zur Produktionsoptimierung unter dem Lean Gedanke, Schlagwort: "5S", nachhaltig, sauber
Aufgabenstellung
Wir sind auf der Suche nach Visitenkarten und Briefpapier für das Unternehmen ourKarto. Nachhaltig, Sauber usw.. Unser Firmenlogo finden Sie anbei.

```html
<!DOCTYPE html>
<html lang="de">
<head>
<meta charset="utf-8">
<title>ourKarto – Visitenkarten</title>
<link rel="stylesheet" href="https://fonts.googleapis.com/css2?family=PT+Sans:wght@400;700&display=swap">
<style>
  :root {
    --backdrop: #2a2a2a;
    --card: #ffffff;
    --green-dark: #1f7a3a;
    --green-mid: #2e9a45;
    --green-light: #4cb84f;
    --ink: #1e1e1e;
    --ink-soft: #3a3a3a;
    --brand-grey: #3d3d3d;
  }
  html, body {
    margin: 0;
    padding: 0;
    width: 1163px;
    height: 1200px;
    overflow: hidden;
    background: var(--backdrop);
    font-family: "PT Sans", Arial, sans-serif;
  }
  .canvas {
    position: relative;
    width: 1163px;
    height: 1200px;
  }
  .card {
    position: absolute;
    width: 666px;
    height: 382px;
    background: var(--card);
    box-shadow: 0 6px 18px rgba(0,0,0,.55);
  }
  .card svg { display: block; width: 100%; height: 100%; }
  .card--front { left: 203px; top: 255px; }
  .card--back  { left: 297px; top: 685px; }
  .brand-name { font-weight: 700; fill: var(--brand-grey); }
  .brand-mark { fill: var(--green-mid); }
  .person-name { font-weight: 700; font-size: 15px; fill: var(--ink); }
  .person-role, .contact { font-size: 11.5px; fill: var(--ink-soft); }
</style>
</head>
<body>
<main class="canvas">

  <section class="card card--front" aria-label="Visitenkarte Vorderseite">
    <svg viewBox="0 0 515 296" xmlns="http://www.w3.org/2000/svg">
      <defs>
        <linearGradient id="greenFront" x1="0" y1="0" x2="0" y2="1">
          <stop offset="0" stop-color="var(--green-dark)"/>
          <stop offset="1" stop-color="var(--green-light)"/>
        </linearGradient>
      </defs>
      <path class="wave-field" d="M0,0 H515 V98 C470,104 400,102 330,74 C250,40 120,18 0,58 Z" fill="url(#greenFront)"/>
      <path class="wave-stripe" d="M0,72 C120,34 250,58 330,92 C400,118 470,114 515,108 V114 C470,120 400,124 330,100 C250,68 120,44 0,76 Z" fill="var(--green-mid)"/>

      <rect class="brand-mark" x="30" y="95" width="20" height="20" rx="3"/>
      <text class="brand-name" x="56" y="112" font-size="22">ourKarto</text>

      <text class="person-name" x="36" y="178">Jonas Feldmann</text>
      <line class="name-rule" x1="190" y1="173.5" x2="515" y2="173.5" stroke="var(--green-dark)" stroke-width="2.5"/>
      <text class="person-role" x="38" y="198">Geschäftsführer</text>

      <text class="contact" x="38" y="247">Lindenweg 12</text>
      <text class="contact" x="38" y="263">79312 Emmendingen</text>
      <text class="contact" x="38" y="279">Germany</text>

      <text class="contact" x="193" y="262">mail: kontakt@ourkarto.de</text>
      <text class="contact" x="193" y="278">www.ourkarto.de</text>

      <text class="contact" x="357" y="263">tel: 0 76 41 / 12 34 56</text>
      <text class="contact" x="357" y="279">fax: 0 76 41 / 12 34 570</text>
    </svg>
  </section>

  <section class="card card--back" aria-label="Visitenkarte Rückseite">
    <svg viewBox="0 0 515 296" xmlns="http://www.w3.org/2000/svg">
      <defs>
        <linearGradient id="greenBack" x1="0" y1="0" x2="0" y2="1">
          <stop offset="0" stop-color="var(--green-dark)"/>
          <stop offset="1" stop-color="var(--green-light)"/>
        </linearGradient>
      </defs>
      <path class="wave-field" d="M0,0 H515 V168 C470,150 420,140 350,148 C250,160 160,210 0,212 Z" fill="url(#greenBack)"/>
      <path class="wave-stripe" d="M0,222 C160,222 250,172 350,160 C420,152 470,160 515,176 V182 C470,166 420,158 350,166 C250,180 160,226 0,228 Z" fill="var(--green-mid)"/>

      <rect class="brand-mark" x="302" y="210" width="26" height="26" rx="4"/>
      <text class="brand-name" x="336" y="233" font-size="29">ourKarto</text>
    </svg>
  </section>

</main>
</body>
</html>
```